Upmarket building and construction company needs signage

Our building company R Brent Construction, needs signage to put up on the side of our vehicle trailers and on site fencing. We are a building company that specialises in residential construction and carpentry .

I will attach our logo and some inspirational pics for site fencing as well as what our trailer looks like .
Other details i would like on the sign are our
( email) rbrentconstruction@mailbox-example.net
(mobile ) 0493 518 264
(website ) rbrentconstruction. example.net

Target Market(s)

Home owners looking for a reliable local builder who produces good quality work. I have attached some inspirational pics.

Industry/Entity Type

Building and Construction

Colors

Designer to choose colors to be used in the design.

Requirements
Must have
• Our logo, contact information
Nice to have
• We would like the design to have elements of being Elegant, Serious, Modern, Professional, Masculine, Conservative and Upmarket.

```html
<!DOCTYPE html>
<html lang="en">
<head>
<meta charset="utf-8">
<title>R Brent Construction – Site Fence Signage</title>
<link rel="stylesheet" href="https://fonts.googleapis.com/css2?family=Jost:wght@400&family=PT+Sans:wght@400&display=swap">
<style>
  :root {
    --page: #ffffff;
    --slate: #3c4150;
    --slate-light: #555b6b;
    --line-grey: #6e7484;
    --gold: #e2d58e;
    --ink-light: #ffffff;
  }
  * { margin: 0; padding: 0; box-sizing: border-box; }
  html, body {
    width: 927px;
    height: 1200px;
    overflow: hidden;
    background: var(--page);
  }
  .canvas {
    position: relative;
    width: 927px;
    height: 1200px;
  }
  .sign {
    position: absolute;
    left: 37px;
    top: 91px;
    width: 847px;
    height: 446px;
    background: var(--slate);
    overflow: hidden;
  }
  .texture {
    position: absolute;
    inset: 0;
    width: 100%;
    height: 100%;
  }
  .contact {
    position: absolute;
    left: 32px;
    top: 96px;
    color: var(--ink-light);
  }
  .contact__phone {
    font-family: "Jost", sans-serif;
    font-size: 25px;
    letter-spacing: 3px;
    line-height: 1;
    margin-bottom: 15px;
  }
  .contact__line {
    font-family: "PT Sans", sans-serif;
    font-size: 17px;
    line-height: 1;
    margin-bottom: 18px;
  }
  .brand {
    position: absolute;
    right: 59px;
    top: 300px;
    text-align: right;
    color: var(--gold);
    font-family: "Jost", sans-serif;
    font-weight: 400;
  }
  .brand__name {
    display: flex;
    align-items: center;
    justify-content: flex-end;
    gap: 12px;
    font-size: 29px;
    letter-spacing: 2px;
    line-height: 1;
  }
  .brand__mark {
    width: 16px;
    height: 16px;
    background: var(--gold);
  }
  .brand__tagline {
    margin-top: 14px;
    font-size: 20px;
    letter-spacing: 1.6px;
    line-height: 1;
  }
</style>
</head>
<body>
<main class="canvas">
  <section class="sign">
    <svg class="texture" viewBox="0 0 847 446" role="img" aria-label="Fine layered grey line texture along the top, bottom and lower left of the sign">
      <defs>
        <linearGradient id="band-top" x1="0" y1="0" x2="0" y2="1">
          <stop offset="0" stop-color="#555b6b" stop-opacity="0.6"/>
          <stop offset="1" stop-color="#3c4150" stop-opacity="0"/>
        </linearGradient>
        <linearGradient id="band-bottom" x1="0" y1="1" x2="0" y2="0">
          <stop offset="0" stop-color="#555b6b" stop-opacity="0.6"/>
          <stop offset="1" stop-color="#3c4150" stop-opacity="0"/>
        </linearGradient>
        <linearGradient id="ridge" x1="0" y1="1" x2="0.6" y2="0">
          <stop offset="0" stop-color="#6e7484" stop-opacity="0.45"/>
          <stop offset="1" stop-color="#3c4150" stop-opacity="0"/>
        </linearGradient>
      </defs>
      <polygon points="0,0 847,0 847,8 120,44 0,28" fill="url(#band-top)"/>
      <polygon points="0,146 0,400 500,400 300,270 90,230" fill="url(#ridge)"/>
      <polygon points="0,446 0,405 400,410 847,385 847,446" fill="url(#band-bottom)"/>
    </svg>

    <div class="contact">
      <p class="contact__phone">0493 518 264</p>
      <p class="contact__line">email: rbrentconstruction@mailbox-example.net</p>
      <p class="contact__line">rbrentconstruction. example.net</p>
    </div>

    <div class="brand">
      <p class="brand__name"><span class="brand__mark"></span>R BRENT CONSTRUCTION</p>
      <p class="brand__tagline">BUILDING AND CARPENTRY</p>
    </div>
  </section>
</main>
</body>
</html>
```